Poster for International workers day 2021 ( May day 1 )

We're looking for poster for for ( International workers day 2021 - May day ) to post on LinkedIn and insta with our company logo and content, I have attached our logo in .png format and sample content for the poster.

```html
<!DOCTYPE html>
<html lang="en">
<head>
<meta charset="utf-8">
<title>International Workers' Day – 1 May</title>
<link href="https://fonts.googleapis.com/css2?family=Jost:wght@500;600;700&family=Montserrat+Alternates:ital,wght@1,300&family=Playfair+Display:ital,wght@1,700&display=swap" rel="stylesheet">
<style>
  :root {
    --sky-top: #0d6d90;
    --sky-mid: #0f4f6f;
    --sky-bottom: #0a2035;
    --white: #ffffff;
    --lime: #8dc63f;
    --ice: #8fd3df;
  }
  * { margin: 0; padding: 0; box-sizing: border-box; }
  html, body { width: 1200px; height: 1200px; overflow: hidden; }
  .poster {
    position: relative;
    width: 1200px;
    height: 1200px;
    overflow: hidden;
    font-family: "Jost", "Century Gothic", sans-serif;
    color: var(--white);
  }
  .backdrop {
    position: absolute;
    inset: 0;
    background: linear-gradient(180deg, var(--sky-top) 0%, var(--sky-mid) 45%, var(--sky-bottom) 100%);
  }
  .frame {
    position: absolute;
    left: 70px; top: 70px;
    width: 1060px; height: 1060px;
    border: 4px solid var(--white);
  }
  .heading {
    position: absolute;
    top: 136px; left: 0; right: 0;
    text-align: center;
    font-weight: 700;
    font-size: 78px;
    line-height: 1;
    letter-spacing: 1px;
  }
  .occasion {
    position: absolute;
    top: 254px; left: 0; right: 0;
    text-align: center;
    font-weight: 500;
    font-size: 68px;
    line-height: 1;
    color: var(--lime);
    letter-spacing: -1px;
  }
  .date-row {
    position: absolute;
    top: 340px; left: 165px;
    width: 866px; height: 96px;
    display: flex;
    align-items: center;
    justify-content: space-between;
  }
  .date-rule {
    width: 272px;
    height: 3px;
    background: var(--white);
  }
  .date {
    font-weight: 500;
    font-size: 98px;
    line-height: 1;
    color: var(--ice);
    letter-spacing: -2px;
  }
  .quote {
    position: absolute;
    top: 570px; left: 0; right: 0;
    text-align: center;
    font-family: "Montserrat Alternates", "Montserrat", sans-serif;
    font-style: italic;
    font-weight: 300;
    font-size: 45px;
    line-height: 62px;
    letter-spacing: 1.5px;
  }
  .quote-mark {
    position: absolute;
    font-family: "Playfair Display", Georgia, serif;
    font-style: italic;
    font-weight: 700;
    font-size: 120px;
    line-height: 1;
    color: var(--white);
  }
  .quote-mark--open { left: 220px; top: 505px; }
  .quote-mark--close { left: 920px; top: 810px; }
  .brand {
    position: absolute;
    top: 980px; left: 0; right: 0;
    text-align: center;
    font-weight: 600;
    font-size: 72px;
    line-height: 1;
    letter-spacing: 2px;
    color: var(--ice);
  }
</style>
</head>
<body>
  <main class="poster">
    <div class="backdrop" role="img" aria-label="Blue gradient background with a faint repeating pattern of film, camera, music and theatre-mask icons"></div>
    <div class="frame"></div>

    <h1 class="heading">Let's Celebrate</h1>
    <h2 class="occasion">INTERNATIONAL WORKER'S DAY</h2>

    <div class="date-row">
      <span class="date-rule"></span>
      <span class="date">1 MAY</span>
      <span class="date-rule"></span>
    </div>

    <span class="quote-mark quote-mark--open">“</span>
    <p class="quote">
      The success of each entity<br>
      and organization is<br>
      because of the people<br>
      who work hard together.
    </p>
    <span class="quote-mark quote-mark--close">”</span>

    <div class="brand">REELCREST</div>
  </main>
</body>
</html>
```